Letterhead & Business Card for our Professional Practice (Financial Services)

We are looking for someone to design a letterhead and business card for our business, which is a professional practice called Corvel Brook Capital Limited. The website is at www.corvelbrookcapitel.example.

The letterhead needs to have: (a) our logo (b) address (c) telephone number (d) email address and (e) our company number.

We would like the stationary to be consistent with the website.

I have attached the logo in EPS and PNG format.

Target Market(s)

Professional services, large commercial enterprises, financial services

Industry/Entity Type

Financial Service

Font styles to use
Serif

Colors
3176b5
f04a50

Requirements
Must have
• Be consistent with our website located at www.corvelbrookcapital.example
• Be in the following formats:
• 1. Word template for the letterhead
• 2. PDF for the letterhead with setup and bleeds required at www.presslyne88.example
• 3. PDF for the business card with setup and bleeds required at www.presslyne88.example
Nice to have
• Something with a really interesting design that says "these guys are professional but dynamic and interesting"
Should not have
• Boring

```html
<!DOCTYPE html>
<html lang="en">
<head>
<meta charset="utf-8">
<title>Corvel Brook Capital – Stationery</title>
<link href="https://fonts.googleapis.com/css2?family=PT+Sans+Narrow&family=Source+Sans+3:wght@400&family=Jost:wght@400&family=Pinyon+Script&display=swap" rel="stylesheet">
<style>
  :root{
    --backdrop:#a9a8a9;
    --paper:#f5f4f3;
    --navy:#1b3a6d;
    --red:#d3202b;
    --ink:#4a4a4a;
    --ink-dark:#1e1e1e;
    --motif-grey:rgba(201,204,214,.45);
    --motif-pink:rgba(236,195,200,.45);
  }
  *{margin:0;padding:0;box-sizing:border-box}
  html,body{width:1200px;height:771px;overflow:hidden;background:var(--backdrop)}
  .canvas{position:relative;width:1200px;height:771px}
  .sheet{position:absolute;background:var(--paper);overflow:hidden;box-shadow:0 0 6px rgba(0,0,0,.25)}
  .motif{position:absolute;background:linear-gradient(120deg,var(--motif-grey),var(--motif-pink))}
  .brand{position:absolute;display:flex;align-items:center;gap:6px;
    font-family:"PT Sans Narrow",sans-serif;font-size:18px;color:var(--navy);white-space:nowrap}
  .brand-square{width:10px;height:10px;background:var(--red)}

  .letterhead{left:61px;top:33px;width:496px;height:701px}
  .letterhead .motif{left:89px;top:228px;width:356px;height:270px}
  .letterhead .brand{left:0;right:0;top:83px;justify-content:center}
  .salutation{position:absolute;left:36px;top:196px;font-family:"Source Sans 3",sans-serif;font-size:13.5px;color:var(--ink)}
  .letter-body{position:absolute;left:36px;top:237px;width:424px;font-family:"Source Sans 3",sans-serif;
    font-size:8.2px;line-height:12px;color:var(--ink);text-align:justify}
  .letter-body p{margin-bottom:12px}
  .closing{position:absolute;left:36px;top:490px;font-family:"Source Sans 3",sans-serif;font-size:7.8px;color:var(--ink)}
  .signature{position:absolute;left:49px;top:507px;width:66px;height:26px;
    background:linear-gradient(90deg,rgba(40,40,50,.12),rgba(40,40,50,.05))}
  .signatory{position:absolute;left:53px;top:543px;font-family:"Source Sans 3",sans-serif;font-size:8.5px;line-height:13px;color:var(--ink)}

  .company-line{font-family:"Jost",sans-serif;font-size:8.5px;color:var(--ink-dark);white-space:nowrap}
  .address{font-family:"Jost",sans-serif;font-size:7.6px;color:var(--ink-dark);white-space:nowrap}
  .rule{height:1px;background:linear-gradient(90deg,#6f6f6f,rgba(111,111,111,.2))}
  .contacts{display:flex;gap:5px;align-items:center;font-family:"Jost",sans-serif;font-size:7.8px;color:var(--ink-dark);white-space:nowrap}
  .contact{display:flex;align-items:center;gap:2px}
  .contact svg{width:11px;height:11px}
  .letter-footer{position:absolute;left:29px;top:633px;width:300px}
  .letter-footer .rule{margin:4px 0 5px;width:270px}

  .slip{left:586px;top:480px;width:561px;height:254px}
  .slip .motif{left:254px;top:0;width:307px;height:254px}
  .slip .brand{left:27px;top:54px}
  .slip-footer{position:absolute;left:29px;top:203px;width:496px}
  .slip-footer .rule{margin:4px 0 5px;background:#6f6f6f}
  .compliments{position:absolute;right:36px;top:175px;font-family:"Pinyon Script",cursive;font-size:35px;color:var(--navy);white-space:nowrap}
</style>
</head>
<body>
<main class="canvas">

  <section class="sheet letterhead" aria-label="Letterhead">
    <div class="motif" role="img" aria-label="Faint grey and pink decorative motif"></div>

    <div class="brand"><span class="brand-square"></span>Corvel Brook Capital</div>

    <p class="salutation">Dear Mr. Pemberly,</p>

    <div class="letter-body">
      <p>Lorem ipsum dolor sit amet, consectetur adipiscing elit. Donec orci purus, luctus vitae dignissim eu, iaculis sed purus. Vivamus faucibus, ipsum nec aliquet viverra, leo mauris condimentum ligula, sit amet sagittis enim ligula quis arcu. Nam egestas tortor id nisi porttitor mattis. In tortor ante, ultricies in suscipit a, tempus non massa. Vivamus et auctor mi. Fusce vel massa nulla. Phasellus nec eros mauris, et scelerisque orci.</p>
      <p>Donec malesuada orci vitae nulla accumsan porta a id massa. Quisque accumsan iaculis magna sit amet fringilla. Maecenas consequat, magna eget tincidunt semper, odio nibh rutrum mi, id feugiat ante nisi eu risus. Vestibulum nunc orci, rhoncus a placerat in, ultricies in mi. Cras mattis varius eros, vel fringilla nisi suscipit eget. Quisque scelerisque sagittis nulla at porttitor.</p>
      <p>Sed id augue vitae urna euismod commodo aliquet a quam. Pellentesque arcu velit, cursus et malesuada ut, consequat et diam. Nullam erat sem, rhoncus id ullamcorper vitae, rhoncus et arcu. In ultricies ultricies nulla, ut rutrum nisi iaculis at. Donec eu magna a metus ornare faucibus. Fusce aliquet faucibus ultricies. Morbi semper, est id tincidunt gravida, sem arcu adipiscing lacus, ac bibendum nulla leo eu purus. Quisque nec diam sed risus consectetur a ccumsan quis quis nibh. Vestibulum id purus lorem.</p>
      <p>It is a long established fact that a reader will be distracted by the readable content of a page when looking at its layout. The point of using Lorem Ipsum is that it has a more-or-less normal distribution of letters, as opposed to using 'Content here, content here', making it look like readable English. Many desktop publishing packages</p>
    </div>

    <p class="closing">Sincerely,</p>
    <div class="signature" role="img" aria-label="Handwritten signature"></div>
    <p class="signatory">Alan Pemberly<br>CEO/ Founder</p>

    <footer class="letter-footer">
      <p class="company-line">Corvel Brook Capital Limited. Registered in England &amp; Wales 09214736</p>
      <p class="address">14-16 Harlow Lane, Eastmere, Dunshire, DN7 2QP</p>
      <div class="rule"></div>
      <div class="contacts">
        <span class="contact"><svg viewBox="0 0 12 12"><circle cx="6" cy="6" r="6" fill="var(--navy)"/><path d="M3.6 3.2l1.2-.4.8 1.6-.8.6c.4.9 1 1.5 1.9 1.9l.6-.8 1.6.8-.4 1.2C6 8.2 3.8 6 3.6 3.2z" fill="#fff"/></svg>01632 960418</span>
        <span class="contact"><svg viewBox="0 0 12 12"><circle cx="6" cy="6" r="6" fill="var(--navy)"/><rect x="3" y="4" width="6" height="4.2" fill="#fff"/><path d="M3 4l3 2.3L9 4" fill="none" stroke="var(--navy)" stroke-width=".7"/></svg>info@corvelbrookcapitel.example</span>
        <span class="contact"><svg viewBox="0 0 12 12"><circle cx="6" cy="6" r="6" fill="var(--navy)"/><circle cx="6" cy="6" r="3.2" fill="none" stroke="#fff" stroke-width=".8"/><path d="M2.8 6h6.4M6 2.8c-1.5 1.8-1.5 4.6 0 6.4M6 2.8c1.5 1.8 1.5 4.6 0 6.4" fill="none" stroke="#fff" stroke-width=".6"/></svg>corvelbrookcapitel.example</span>
      </div>
    </footer>
  </section>

  <section class="sheet slip" aria-label="Compliments slip">
    <div class="motif" role="img" aria-label="Faint grey and pink decorative motif"></div>

    <div class="brand"><span class="brand-square"></span>Corvel Brook Capital</div>

    <p class="compliments">With Compliments</p>

    <footer class="slip-footer">
      <p class="address">14-16 Harlow Lane, Eastmere, Dunshire, DN7 2QP</p>
      <div class="rule"></div>
      <div class="contacts">
        <span class="contact"><svg viewBox="0 0 12 12"><circle cx="6" cy="6" r="6" fill="var(--navy)"/><path d="M3.6 3.2l1.2-.4.8 1.6-.8.6c.4.9 1 1.5 1.9 1.9l.6-.8 1.6.8-.4 1.2C6 8.2 3.8 6 3.6 3.2z" fill="#fff"/></svg>01632 960418</span>
        <span class="contact"><svg viewBox="0 0 12 12"><circle cx="6" cy="6" r="6" fill="var(--navy)"/><rect x="3" y="4" width="6" height="4.2" fill="#fff"/><path d="M3 4l3 2.3L9 4" fill="none" stroke="var(--navy)" stroke-width=".7"/></svg>info@corvelbrookcapitel.example</span>
        <span class="contact"><svg viewBox="0 0 12 12"><circle cx="6" cy="6" r="6" fill="var(--navy)"/><circle cx="6" cy="6" r="3.2" fill="none" stroke="#fff" stroke-width=".8"/><path d="M2.8 6h6.4M6 2.8c-1.5 1.8-1.5 4.6 0 6.4M6 2.8c1.5 1.8 1.5 4.6 0 6.4" fill="none" stroke="#fff" stroke-width=".6"/></svg>corvelbrookcapitel.example</span>
      </div>
    </footer>
  </section>

</main>
</body>
</html>
```